Upmarket building and construction company needs signage

Our building company R Brent Construction, needs signage to put up on the side of our vehicle trailers and on site fencing. We are a building company that specialises in residential construction and carpentry .

I will attach our logo and some inspirational pics for site fencing as well as what our trailer looks like .
Other details i would like on the sign are our
( email) rbrentconstruction@mailbox-example.net
(mobile ) 0493 518 264
(website ) rbrentconstruction. example.net

Target Market(s)

Home owners looking for a reliable local builder who produces good quality work. I have attached some inspirational pics.

Industry/Entity Type

Building and Construction

Colors

Designer to choose colors to be used in the design.

Requirements
Must have
• Our logo, contact information
Nice to have
• We would like the design to have elements of being Elegant, Serious, Modern, Professional, Masculine, Conservative and Upmarket.

```html
<!DOCTYPE html>
<html lang="en">
<head>
<meta charset="utf-8">
<title>R Brent Construction – Site Signage</title>
<link rel="stylesheet" href="https://fonts.googleapis.com/css2?family=Montserrat:wght@300;400&display=swap">
<style>
  :root {
    --backdrop: #333333;
    --sign-grey: #828282;
    --sign-ink: #ffffff;
    --decor-tone: #a3a3a3;
  }
  * { margin: 0; padding: 0; box-sizing: border-box; }
  html, body {
    width: 900px;
    height: 1200px;
    overflow: hidden;
    background: var(--backdrop);
  }
  .canvas {
    position: relative;
    width: 900px;
    height: 1200px;
    background: var(--backdrop);
  }
  .sign {
    position: absolute;
    left: 64px;
    top: 455px;
    width: 772px;
    height: 289px;
    background: var(--sign-grey);
    color: var(--sign-ink);
    font-family: "Montserrat", Arial, sans-serif;
    font-weight: 300;
    overflow: hidden;
  }
  .brand {
    position: absolute;
    left: 40px;
    top: 42px;
    display: flex;
    align-items: center;
    gap: 7px;
    font-size: 12px;
    letter-spacing: 0.04em;
    line-height: 1.2;
    text-transform: uppercase;
  }
  .brand-square {
    width: 10px;
    height: 10px;
    background: var(--sign-ink);
  }
  .brand-name { width: 90px; }
  .contact {
    position: absolute;
    right: 24px;
    top: 44px;
    font-size: 16px;
    line-height: 27px;
    white-space: nowrap;
  }
  .tagline {
    position: absolute;
    left: 40px;
    top: 132px;
    font-size: 31px;
    font-weight: 300;
    line-height: 40px;
  }
  .website {
    position: absolute;
    left: 40px;
    top: 236px;
    font-size: 16px;
    white-space: nowrap;
  }
  .brand-decoration {
    position: absolute;
    left: 486px;
    top: 136px;
    width: 225px;
    height: 153px;
    background: linear-gradient(180deg, var(--sign-grey) 0%, var(--decor-tone) 100%);
  }
</style>
</head>
<body>
  <main class="canvas">
    <section class="sign">
      <div class="brand">
        <span class="brand-square"></span>
        <span class="brand-name">R Brent Construction</span>
      </div>
      <div class="contact">
        <p class="contact-phone">0493 518 264</p>
        <p class="contact-email">rbrentconstruction@mailbox-example.net</p>
      </div>
      <h1 class="tagline">Quality<br>craftsmanship</h1>
      <p class="website">www.rbrentconstruction. example.net</p>
      <div class="brand-decoration" role="img" aria-label="Large brand symbol decoration area"></div>
    </section>
  </main>
</body>
</html>
```